Hip and quirky Indian restaurant Menu

We need a build your own bowl/meal/wrap menu similar to Verdigo others. We would like illustrations if possible of India/veggies/chicken/animals/themes. Please utilize the colors that match the schema of the logos provided. We have included pictures you may use them if you would like to. Menu provided is our old menu.

Target Market(s)

Millenials, Ge

Industry/Entity Type

Retail

Font styles to use
Sans Serif
Decorative

Requirements
Must have
• logical placements for build your own meal options
Nice to have
• Illustrations.

```html
<!DOCTYPE html>
<html lang="en">
<head>
<meta charset="utf-8">
<title>Masala Mela – Build Your Own Menu</title>
<link href="https://fonts.googleapis.com/css2?family=Oswald:wght@500;700&family=Roboto+Condensed:ital,wght@0,300;0,400;0,700;1,400;1,700&display=swap" rel="stylesheet">
<style>
:root{
  --orange:#F9AE41;
  --coral:#EE6240;
  --red:#E8232F;
  --navy:#262459;
  --maroon:#6B1414;
  --white:#ffffff;
}
*{margin:0;padding:0;box-sizing:border-box}
html,body{width:1200px;height:848px;overflow:hidden;background:var(--white)}
.menu{position:relative;width:1200px;height:848px;overflow:hidden;font-family:"Roboto Condensed",Arial,sans-serif;color:var(--maroon)}
.bg{position:absolute;left:0;top:0}
.abs{position:absolute}

.brand{position:absolute;left:66px;top:62px;font-family:"Oswald",sans-serif;font-weight:700;color:var(--navy);font-size:40px;line-height:.95;text-transform:uppercase}

.title{position:absolute;font-family:"Oswald",sans-serif;font-weight:700;line-height:1;text-transform:uppercase;white-space:nowrap;text-align:right}
.title .small{display:block;font-size:30px;text-transform:none}
.title .big{display:block;font-size:40px}
.price{position:absolute;border-radius:50%;color:var(--white);font-family:"Oswald",sans-serif;font-weight:500;font-size:24px;display:flex;align-items:center;justify-content:center;z-index:2}
.price.red{background:var(--red)}
.price.navy{background:var(--navy)}

.photo{position:absolute;width:144px;height:74px;border-radius:72px 72px 0 0}
.photo.bread{background:linear-gradient(#f4e2c0,#d9a860)}
.photo.curry{background:linear-gradient(#c8d08a,#d1622a)}
.photo.slaw{background:linear-gradient(#8a9a4a,#d7a43c)}
.photo.sauce{background:linear-gradient(#6f8a4a,#9a7a3a)}
.photo.redcurry{background:linear-gradient(#b8432a,#7a1f14)}
.photo.chickpea{background:linear-gradient(#d9a64a,#b04a2a)}
.photo.dip{background:linear-gradient(#e8e2da,#9e2a1c)}

.num{position:absolute;font-family:"Oswald",sans-serif;font-weight:700;font-size:62px;line-height:1;color:var(--coral)}
.num.navytxt{color:var(--red)}
.bar{position:absolute;height:27px;background:var(--coral);color:var(--maroon);font-size:21px;font-weight:300;line-height:27px;padding-left:20px;white-space:nowrap}
.bar b{font-weight:700}
.bar i{font-size:14px;font-weight:400;font-style:italic}
.card{position:absolute;background:var(--white);font-weight:700;font-size:13.4px;line-height:17.6px;padding-top:7px}
.card.warm{background:var(--orange)}
.col{position:absolute;white-space:nowrap}
.note{font-size:9px;font-weight:400;line-height:12px}

.k,.v{display:inline-block;width:10px;height:10px;border-radius:50%;background:var(--coral);color:var(--white);font-size:7px;line-height:10px;text-align:center;font-weight:700;vertical-align:1px;margin-left:2px}
.warm .k,.warm .v{background:#F58A45}
.chili{display:inline-block;width:10px;height:4px;background:var(--red);border-radius:0 4px 4px 0;transform:rotate(-40deg);vertical-align:3px;margin-left:3px}

.dishhead{position:absolute;height:24px;background:var(--navy);color:var(--white);font-weight:700;font-size:16px;line-height:24px;padding-left:14px}

.legend{position:absolute;left:782px;top:780px;color:var(--white);font-size:9.5px;line-height:17px}
.legend .row{display:flex;align-items:center;gap:3px}
.legend .halal{font-size:12.5px}
.platter{position:absolute;right:0;bottom:0;width:240px;height:140px;border-radius:160px 0 0 0;background:linear-gradient(135deg,#3d6b2a,#b5652a 55%,#d9a070)}
</style>
</head>
<body>
<main class="menu">

<svg class="bg" width="1200" height="848" viewBox="0 0 1200 848" aria-hidden="true">
  <rect width="1200" height="848" fill="#ffffff"/>
  <path d="M0 448 C80 420 140 360 220 300 C330 215 420 180 520 130 C610 85 690 40 765 0 L765 848 L0 848 Z" fill="#F9AE41"/>
  <path d="M0 584 L640 584 Q732 590 732 690 L732 848 L0 848 Z" fill="#E8232F"/>
  <rect x="765" y="0" width="435" height="848" fill="#262459"/>
  <path d="M765 848 C850 760 990 720 1200 640" fill="none" stroke="#3a3873" stroke-width="2"/>
</svg>

<div class="brand">Masala<br>Mela</div>

<!-- WRAP -->
<div class="title" style="left:330px;top:130px;color:var(--navy);width:206px">
  <span class="small">Build Your</span><span class="big">Own Wrap</span>
</div>
<div class="price red" style="left:544px;top:137px;width:58px;height:58px">8.00</div>
<div class="abs" style="left:452px;top:205px;color:var(--white);font-weight:700;font-size:18px">2 WRAPS</div>

<div class="photo bread" role="img" aria-label="Photo of flaky paratha with butter" style="left:236px;top:238px"></div>
<span class="num" style="left:162px;top:262px">1</span>
<div class="bar" style="left:166px;top:312px;width:234px">Pick <b>Wrap</b></div>
<div class="card" style="left:166px;top:339px;width:234px;height:65px">
  <div class="col" style="left:19px">Paratha<br>Naan<br>Chapati</div>
</div>

<div class="photo curry" role="img" aria-label="Photo of chickpea curry in a bowl" style="left:236px;top:388px"></div>
<span class="num" style="left:84px;top:412px">2</span>
<div class="bar" style="left:86px;top:462px;width:314px">Pick <b>Main Curry</b> <i>(Pick one)</i></div>
<div class="card" style="left:86px;top:488px;width:314px;height:82px">
  <div class="col" style="left:20px">Veg Korma <span class="v">V</span><br>Chana Masala <span class="v">V</span><br>Chicken Tikka Masala <span class="k">K</span><br>Chili Chicken <span class="k">K</span><span class="chili"></span></div>
  <div class="col" style="left:183px">Beef Curry <span class="k">K</span><span class="chili"></span> &nbsp;&nbsp;*+1<br>Double Protein &nbsp;&nbsp;*+2<br><span class="note">*(For premium curry extra)</span></div>
</div>

<div class="photo slaw" role="img" aria-label="Photo of shredded vegetable toppings in a bowl" style="left:566px;top:210px"></div>
<span class="num" style="left:416px;top:234px">3</span>
<div class="bar" style="left:418px;top:284px;width:314px">Pick <b>Toppings</b> <i>(Pick as many)</i></div>
<div class="card" style="left:418px;top:310px;width:314px;height:100px">
  <div class="col" style="left:20px">Green Beans Thoran <span class="v">V</span><br>Cabbage Thoran <span class="k">K</span><span class="v">V</span><br>Chick Pea Salad <span class="k">K</span><span class="v">V</span><br>Cucumber Salad <span class="k">K</span><span class="v">V</span></div>
  <div class="col" style="left:170px">Diced Onion <span class="v">V</span><br>Chopped Bell Pepper <span class="v">V</span><br>Shredded Cheese <span class="k">K</span><br>Cilantro <span class="k">K</span><span class="v">V</span><br>Jalapeno <span class="k">K</span><span class="v">V</span></div>
</div>

<div class="photo sauce" role="img" aria-label="Photo of mint sauce in a small bowl" style="left:566px;top:418px"></div>
<span class="num" style="left:416px;top:442px">4</span>
<div class="bar" style="left:418px;top:492px;width:314px">Pick <b>Sauces</b> <i>(Pick as many)</i></div>
<div class="card" style="left:418px;top:518px;width:314px;height:52px">
  <div class="col" style="left:20px">Original Mint <span class="k">K</span><span class="v">V</span><br>Sweet Tamarind <span class="k">K</span><span class="v">V</span></div>
  <div class="col" style="left:187px">Mango Chilli <span class="k">K</span><span class="v">V</span><span class="chili"></span><br>Tikka Masala <span class="k">K</span><span class="v">V</span></div>
</div>

<!-- TRADITIONAL BOWL -->
<span class="num" style="left:98px;top:592px">1</span>
<div class="bar" style="left:100px;top:640px;width:231px;background:var(--orange)">Pick <b>Main</b></div>
<div class="card" style="left:100px;top:667px;width:231px;height:49px">
  <div class="col" style="left:19px">Naan<br>Paratha</div>
  <div class="col" style="left:110px">Basmati Rice<br>Curry Rice</div>
  <div class="col" style="left:200px;top:24px">+1</div>
</div>
<span class="num" style="left:52px;top:678px">2</span>
<div class="bar" style="left:54px;top:726px;width:277px;background:var(--orange)">Pick <b>Curries</b></div>
<div class="card" style="left:54px;top:754px;width:277px;height:74px;font-weight:400">
  <div class="col" style="left:20px;top:8px">Your choice of <b>1 Veg</b> &amp; <b>1 Meat</b> Dish</div>
  <div class="col" style="left:20px;top:40px;font-weight:700">Additional Dish &nbsp;&nbsp;&nbsp;+2</div>
  <div class="col note" style="left:20px;top:57px;font-style:italic">(Premium dishes are extra.)</div>
</div>

<div class="title" style="left:346px;top:616px;color:var(--white);width:152px">
  <span class="small">Traditional</span><span class="big" style="font-size:44px">Bowl</span>
</div>
<div class="price navy" style="left:504px;top:624px;width:60px;height:60px">8.00</div>

<div class="dishhead" style="left:354px;top:706px;width:168px">Veg Dishes</div>
<div class="card" style="left:354px;top:730px;width:168px;height:98px">
  <div class="col" style="left:13px">Chana Masala <span class="v">V</span><br>Veg Korma <span class="v">V</span><br>Cabbage Thoran <span class="k">K</span><span class="v">V</span><br>Green Beans Thoran <span class="v">V</span></div>
</div>
<div class="dishhead" style="left:530px;top:706px;width:170px">Meat Dishes</div>
<div class="card" style="left:530px;top:730px;width:170px;height:98px">
  <div class="col" style="left:14px">Chicken Tikka Masala <span class="k">K</span><br>Chilli Chicken <span class="k">K</span><span class="chili"></span><br>Tandoori Chicken <span class="k">K</span> <span class="note">(3 Pcs.)</span><br>Beef Curry <span class="k">K</span><span class="chili"></span><br>Mutton Curry <span class="k">K</span></div>
  <div class="col" style="left:146px;top:59px">+1<br>+2</div>
</div>

<!-- SALAD BOWL -->
<div class="platter" role="img" aria-label="Photo of grilled tandoori chicken with lemon and cilantro"></div>

<div class="title" style="left:780px;top:50px;color:var(--white);width:316px">
  <span class="small">Build Your</span><span class="big">Own Salad Bowl</span>
</div>
<div class="price red" style="left:1100px;top:58px;width:58px;height:58px">8.00</div>

<div class="photo redcurry" role="img" aria-label="Photo of red beef curry in a bowl" style="left:974px;top:148px"></div>
<span class="num navytxt" style="left:824px;top:174px">1</span>
<div class="bar" style="left:826px;top:222px;width:312px">Pick <b>Main Curry</b> <i>(Pick one)</i></div>
<div class="card warm" style="left:826px;top:249px;width:312px;height:81px">
  <div class="col" style="left:19px">Veg Korma <span class="v">V</span><br>Chana Masala <span class="v">V</span><br>Chicken Tikka Masala <span class="k">K</span><br>Chili Chicken <span class="k">K</span><span class="chili"></span></div>
  <div class="col" style="left:181px">Beef Curry <span class="k">K</span><span class="chili"></span> &nbsp;&nbsp;*+1<br>Double Protein &nbsp;&nbsp;*+2<br><span class="note">*(For premium curry extra)</span></div>
</div>

<div class="photo chickpea" role="img" aria-label="Photo of chickpea salad" style="left:974px;top:348px"></div>
<span class="num navytxt" style="left:824px;top:374px">2</span>
<div class="bar" style="left:826px;top:422px;width:312px">Pick <b>Toppings</b> <i>(Pick as many)</i></div>
<div class="card warm" style="left:826px;top:448px;width:312px;height:84px">
  <div class="col" style="left:19px">Chick Pea Salad <span class="k">K</span><span class="v">V</span><br>Cucumber Salad <span class="k">K</span><span class="v">V</span><br>Cilantro <span class="k">K</span><span class="v">V</span><br>Jalapeno <span class="k">K</span><span class="v">V</span></div>
  <div class="col" style="left:169px">Diced Onion <span class="v">V</span><br>Chopped Bell Pepper <span class="v">V</span><br>Shredded Cheese <span class="k">K</span></div>
</div>

<div class="photo dip" role="img" aria-label="Photo of red chilli sauce in a white bowl" style="left:974px;top:556px"></div>
<span class="num navytxt" style="left:824px;top:582px">3</span>
<div class="bar" style="left:826px;top:630px;width:312px">Pick <b>Sauces</b> <i>(Pick as many)</i></div>
<div class="card warm" style="left:826px;top:656px;width:312px;height:52px">
  <div class="col" style="left:19px">Original Mint <span class="k">K</span><span class="v">V</span><br>Sweet Tamarind <span class="k">K</span><span class="v">V</span></div>
  <div class="col" style="left:186px">Mango Chilli <span class="k">K</span><span class="v">V</span><span class="chili"></span><br>Tikka Masala <span class="k">K</span><span class="v">V</span></div>
</div>

<div class="legend">
  <div class="row"><span class="k">K</span> - KETO &nbsp;&nbsp;&nbsp;&nbsp;&nbsp;&nbsp;<span class="chili"></span> - SPICY</div>
  <div class="row"><span class="v">V</span> - VEGAN</div>
  <div class="halal">All meat is halal.</div>
</div>

</main>
</body>
</html>
```